Birchline Heating & Air

I need a business card made for my company. I would like my new logo for Birchline Heating and Air on the front and my Garage Door on the back.
Front to say -Heating & Air Conditioning , Mini Splits and Heat Pumps, Hydronic In-Floor Heat. Locally Owned and Operated! Licensed, Boned and Insured. Free Estimates on new equipment. 715-408-2159
BGD Back Card, change phone# to 651-374-5810. Remove Commercial and residential and fully sticked vans lines.

```html
<!DOCTYPE html>
<html lang="en">
<head>
<meta charset="utf-8">
<title>Birchline Heating &amp; Air – Business Card</title>
<link href="https://fonts.googleapis.com/css2?family=Archivo:ital,wght@0,400;0,500;0,800;0,900;1,900&display=swap" rel="stylesheet">
<style>
  :root {
    --red: #e8301f;
    --blue: #0f4f9c;
    --plum: #8c4468;
    --white: #ffffff;
    --stage: #d8d8d8;
    --brand-gradient: linear-gradient(135deg, var(--red) 18%, var(--plum) 55%, var(--blue) 92%);
  }
  * { box-sizing: border-box; margin: 0; padding: 0; }
  html, body {
    width: 1200px; height: 846px; overflow: hidden;
    background: var(--stage);
    font-family: "Archivo", Arial, sans-serif;
  }
  .sheet {
    position: relative; width: 1200px; height: 846px;
    display: flex; justify-content: center; align-items: center; gap: 90px;
  }
  .card {
    position: relative; width: 400px; height: 700px; overflow: hidden;
    box-shadow: 0 8px 24px rgba(0,0,0,.18);
  }
  .card--front { background: var(--white); }
  .card--back { background: var(--brand-gradient); }

  .brand {
    position: absolute; left: 0; right: 0; top: 64px;
    text-align: center; line-height: 1;
    font-weight: 900; text-transform: uppercase;
  }
  .brand__name { display: block; font-size: 62px; letter-spacing: -1px; }
  .brand__sub { display: block; font-size: 32px; margin-top: 8px; letter-spacing: 1px; }
  .card--front .brand { color: var(--blue); }
  .card--back .brand { color: var(--white); }

  .services {
    position: absolute; left: 44px; right: 30px; top: 210px;
    list-style: none; font-size: 19px; line-height: 1.42; font-weight: 500;
  }
  .services li { white-space: nowrap; }
  .services li::before { content: "•"; margin-right: 4px; }
  .card--front .services { color: var(--blue); }
  .card--front .services li::before { color: var(--red); }
  .card--back .services { color: var(--white); }

  .offer {
    position: absolute; left: 32px; width: 336px; height: 170px;
    border-radius: 30px; border: 2px solid;
  }
  .card--front .offer { top: 372px; border-color: var(--blue); }
  .card--back .offer { top: 318px; border-color: var(--white); }
  .offer__tab {
    position: absolute; top: -2px; right: -2px; width: 282px; height: 84px;
    border-radius: 0 30px 0 30px;
    display: flex; flex-direction: column; justify-content: center; align-items: center;
    text-transform: uppercase; line-height: 1.15; white-space: nowrap;
  }
  .card--front .offer__tab { background: var(--brand-gradient); color: var(--white); }
  .card--back .offer__tab { background: var(--white); color: var(--plum); }
  .offer__headline { font-weight: 900; font-size: 21px; }
  .offer__detail { font-weight: 400; font-size: 19px; letter-spacing: .5px; }
  .offer__phone {
    position: absolute; left: 18px; right: 12px; bottom: 20px;
    display: flex; align-items: center; gap: 10px; white-space: nowrap;
    font-weight: 900; font-style: italic; font-size: 32px; line-height: 1; letter-spacing: .5px;
  }
  .card--front .offer__phone { color: var(--blue); }
  .card--back .offer__phone { color: var(--white); }
  .offer__phone svg { width: 38px; height: 38px; flex: none; }

  .web-band {
    position: absolute; left: 0; right: 0; bottom: 0; height: 138px;
    background: var(--brand-gradient); border-top-right-radius: 60px;
    color: var(--white); text-align: center; font-weight: 900;
    display: flex; flex-direction: column; justify-content: center;
  }
  .web-band__label { font-size: 26px; text-transform: uppercase; }
  .web-band__url { font-size: 21px; margin-top: 6px; }

  .contact {
    position: absolute; left: 0; right: 0; top: 548px;
    text-align: center; color: var(--white); font-weight: 900; font-size: 18px; line-height: 1.5;
  }
  .save-tag {
    position: absolute; left: 50%; bottom: 30px; transform: translateX(-50%);
    background: var(--white); color: var(--red); white-space: nowrap;
    font-weight: 900; font-size: 17px; text-transform: uppercase;
    padding: 8px 26px; border-radius: 0 18px 0 18px;
  }
</style>
</head>
<body>
<main class="sheet">

  <section class="card card--front" aria-label="Front of card">
    <h1 class="brand">
      <span class="brand__name">Birchline</span>
      <span class="brand__sub">Heating &amp; Air</span>
    </h1>
    <ul class="services">
      <li>Heating &amp; Air Conditioning</li>
      <li>Mini Splits and Heat Pumps</li>
      <li>Hydronic In-Floor Heat</li>
      <li>Locally Owned and Operated!</li>
      <li>Licensed, Boned and Insured</li>
    </ul>
    <div class="offer">
      <div class="offer__tab">
        <span class="offer__headline">— Free Estimates —</span>
        <span class="offer__detail">On New Equipment</span>
      </div>
      <p class="offer__phone">
        <svg viewBox="0 0 48 48" aria-hidden="true">
          <path d="M14 6c3 0 4 7 5 10s-3 4-3 6 6 11 9 11 3-4 6-3 9 2 9 5-4 7-8 7C20 42 6 27 6 14c0-4 4-8 8-8z" fill="var(--blue)"/>
          <path d="M30 8a12 12 0 0 1 10 10M30 15a6 6 0 0 1 4 4" stroke="var(--red)" stroke-width="3" fill="none" stroke-linecap="round"/>
        </svg>
        715-408-2159
      </p>
    </div>
    <footer class="web-band">
      <span class="web-band__label">Visit Our Website</span>
      <span class="web-band__url">www.BirchlineGarageDoor.com</span>
    </footer>
  </section>

  <section class="card card--back" aria-label="Back of card">
    <h2 class="brand">
      <span class="brand__name">Birchline</span>
      <span class="brand__sub">Heating &amp; Air</span>
    </h2>
    <ul class="services">
      <li>Same Day &amp; Emergency Service</li>
      <li>All Major Brands</li>
      <li>Locally Owned and Operated!</li>
    </ul>
    <div class="offer">
      <div class="offer__tab">
        <span class="offer__headline">— Free —</span>
        <span class="offer__detail">Service Call</span>
      </div>
      <p class="offer__phone">
        <svg viewBox="0 0 48 48" aria-hidden="true">
          <path d="M14 6c3 0 4 7 5 10s-3 4-3 6 6 11 9 11 3-4 6-3 9 2 9 5-4 7-8 7C20 42 6 27 6 14c0-4 4-8 8-8z" fill="var(--white)"/>
          <path d="M30 8a12 12 0 0 1 10 10M30 15a6 6 0 0 1 4 4" stroke="var(--white)" stroke-width="3" fill="none" stroke-linecap="round"/>
        </svg>
        651-374-5810
      </p>
    </div>
    <p class="contact">
      birchlinegaragedoor@mailbox.com<br>
      www.BirchlineGarageDoor.com
    </p>
    <span class="save-tag">Save This Card!</span>
  </section>

</main>
</body>
</html>
```